Bolt Ridge Hoist Service Business Cards

I need a business card for "Bolt Ridge Hoist and Tackle"

Boltridge2023@hoistmail.example

Hoist Works LLC, Bolt Ridge Hoist and Tackle LLC

555.204.7186 | www.BOLTRIDGEHOISTS.example

Central Indiana & Northeast Ohio

(IN) 23810 Meadow Lane Noblesville, IN 46099

(OH) 4150 Dunmore Street Akron, Ohio 44397

Contact Information for Business Card

Colors
0094D4
00A9DD
6FCCEA
C7EBF8
E9F6FB
59FF00
82FF00
B8FF75
E3FFCB
F4FFEA
EE7325
F08F49
F5BC92
FAE3D3
FDF4ED
EB3D1F
EC4F4E
F09395
F8D3D4
FCEDEE
E54698
E96AAD
F1A4CE
F9D9EA
FCEFF6
A7469A
B969AE
D3A5CF
EDDBEB
F8F0F9

```html
<!DOCTYPE html>
<html lang="en">
<head>
<meta charset="utf-8">
<title>Bolt Ridge Hoist and Tackle – Business Cards</title>
<link href="https://fonts.googleapis.com/css2?family=Exo+2:wght@700;800&family=Poppins:wght@400;600&display=swap" rel="stylesheet">
<style>
  :root {
    --bg: #3b4049;
    --card-white: #ffffff;
    --accent: #eb3d1f;
    --ink: #1c1c1c;
    --black: #0d0d0d;
    --rule: #9a9a9a;
    --logo-grey: #d6d6d6;
    --illus-grey: #8d8f93;
    --illus-green: #3cb54a;
  }
  html, body {
    margin: 0;
    width: 1200px;
    height: 900px;
    overflow: hidden;
    background: var(--bg);
  }
  .sheet {
    position: relative;
    width: 1200px;
    height: 900px;
  }
  .card {
    position: absolute;
    top: 290px;
    width: 560px;
    height: 320px;
    overflow: hidden;
    box-shadow: 0 12px 30px rgba(0,0,0,.45);
  }
  .card--front { left: 30px; background: var(--card-white); }
  .card--back  { left: 610px; background: radial-gradient(ellipse at 60% 40%, #1c1c1c, var(--black) 70%); }

  .card__shapes { position: absolute; inset: 0; }

  .front__heading {
    position: absolute;
    left: 22px;
    top: 18px;
    margin: 0;
    font: 800 19px/1.15 "Exo 2", sans-serif;
    color: #fff;
    text-transform: uppercase;
    letter-spacing: .3px;
  }
  .front__contact {
    position: absolute;
    left: 22px;
    top: 112px;
    width: 305px;
    font: 400 12px/1.6 "Poppins", sans-serif;
    color: var(--ink);
    white-space: nowrap;
  }
  .front__contact p { margin: 0; }
  .contact-line { display: flex; align-items: center; gap: 7px; }
  .contact-line svg { flex: none; }
  .front__region {
    margin-top: 6px !important;
    font-weight: 600;
    font-size: 12.5px;
  }
  .front__rule {
    position: absolute;
    left: 22px;
    top: 232px;
    width: 250px;
    height: 1px;
    background: var(--rule);
  }
  .front__web {
    position: absolute;
    left: 16px;
    top: 291px;
    display: flex;
    align-items: center;
    gap: 8px;
    font: 400 12.5px/1 "Poppins", sans-serif;
    color: #fff;
    letter-spacing: .3px;
  }
  .front__illustration {
    position: absolute;
    left: 345px;
    top: 110px;
    width: 188px;
    height: 165px;
    background: linear-gradient(135deg, #b8b9bc 0%, var(--illus-grey) 35%, #d9563d 60%, var(--illus-green) 100%);
    border-radius: 4px;
    opacity: .85;
  }
  .back__name {
    position: absolute;
    left: 0;
    right: 0;
    top: 122px;
    margin: 0;
    text-align: center;
    font: 800 62px/1 "Exo 2", sans-serif;
    color: var(--logo-grey);
    text-transform: uppercase;
    letter-spacing: 2px;
  }
</style>
</head>
<body>
<main class="sheet">

  <section class="card card--front" aria-label="Business card front">
    <svg class="card__shapes" width="560" height="320" viewBox="0 0 560 320" aria-hidden="true">
      <polygon points="0,0 370,0 370,66 335,100 0,100" fill="var(--accent)"/>
      <polygon points="480,0 560,0 560,38 510,38" fill="var(--black)"/>
      <polygon points="0,278 285,278 250,320 0,320" fill="var(--black)"/>
      <polygon points="268,300 560,300 560,320 252,320" fill="var(--accent)"/>
      <polygon points="510,300 560,250 560,300" fill="var(--black)"/>
    </svg>

    <h1 class="front__heading">Hoist Works LLC<br>Bolt Ridge Hoist and Tackle LLC</h1>

    <div class="front__contact">
      <div class="contact-line">
        <svg width="13" height="13" viewBox="0 0 14 14" aria-hidden="true">
          <circle cx="7" cy="7" r="7" fill="var(--accent)"/>
          <path d="M4.6 3.6l1.3 1.3-.7 1a5 5 0 0 0 2.9 2.9l1-.7 1.3 1.3-.9 1.1C6.8 10.3 3.7 7.2 3.5 4.5z" fill="#fff"/>
        </svg>
        <span>555.204.7186</span>
      </div>
      <div class="contact-line">
        <svg width="13" height="13" viewBox="0 0 14 14" aria-hidden="true">
          <circle cx="7" cy="7" r="7" fill="var(--accent)"/>
          <rect x="3.5" y="4.5" width="7" height="5" fill="none" stroke="#fff" stroke-width="1"/>
          <path d="M3.5 4.5L7 7.3l3.5-2.8" fill="none" stroke="#fff" stroke-width="1"/>
        </svg>
        <span>Boltridge2023@hoistmail.example</span>
      </div>
      <p class="front__region">Central Indiana &amp; Northeast Ohio</p>
      <p class="front__address">(IN) 23810 Meadow Lane Noblesville, IN 46099</p>
      <p class="front__address">(OH) 4150 Dunmore Street Akron, Ohio 44397</p>
    </div>
    <div class="front__rule"></div>

    <div class="front__illustration" role="img" aria-label="Illustration of a red boom truck crane and a green mobile crane in front of a grey steel structure, with the company name on a hanging sign"></div>

    <div class="front__web">
      <svg width="14" height="14" viewBox="0 0 14 14" aria-hidden="true">
        <circle cx="7" cy="7" r="7" fill="var(--accent)"/>
        <circle cx="7" cy="7" r="4" fill="none" stroke="#fff" stroke-width=".9"/>
        <path d="M3 7h8M7 3c-1.6 2.4-1.6 5.6 0 8M7 3c1.6 2.4 1.6 5.6 0 8" fill="none" stroke="#fff" stroke-width=".9"/>
      </svg>
      <span>WWW.BOLTRIDGEHOISTS.EXAMPLE</span>
    </div>
  </section>

  <section class="card card--back" aria-label="Business card back">
    <p class="back__name">Bolt Ridge</p>
  </section>

</main>
</body>
</html>
```